Simple Logo Design for Semi-Clear Plastic Frosted Card stock

Create a business card on frosted plastic. compliment existing logo elements with a tree trunk, roots, or seed at the lower half and the full logo both on the front.

Contact information will go on a solid portion of the back of this design since this card stock is semi-transparent.

It is important to consider this plastic card stock medium in your design. I found helpful tips and guides listed at velnacard.example: be careful to understand ink printed on plastic cards cannot have too much of a consistent print area or risks peeling and fine lines can easily scratch off.
Updates

2" x 3.5" 20PT Clear Plastic Business cards with Round corners Please get info or templates here: https://www.velnacard.example/product-detail/2-x-35-20pt-clear-plastic-business-cards-with-round-corners

Target Market(s)

Not for profit- religion

Industry/Entity Type

Business

Contact Information for Business Card

Must include complementary elements to the existing logo

Font styles to use
Decorative

Colors
000000

Requirements
Must have
• Elements of community, nature and oneness. Such as: seed, roots, tree trunk, etc.
• Three lines of space on the back for Name, Title, Phone Number.
Nice to have
• I like a light use of decorative elements
Should not have
• No eyes, from faces or animals.

```html
<!DOCTYPE html>
<html lang="en">
<head>
<meta charset="utf-8">
<title>Groundedpath Business Card – Frosted Plastic</title>
<link rel="stylesheet" href="https://fonts.googleapis.com/css2?family=Montserrat:wght@400;600&family=Lato:wght@300;400&display=swap">
<style>
  :root {
    --stage: #4b423b;
    --card-light: #cbc7c2;
    --card-dark: #3b3734;
    --card-dark-edge: rgba(255,255,255,0.28);
    --ink-dark: #2b2b2b;
    --ink-light: #ffffff;
    --brand-teal: #3c6e78;
    --caption: #ffffff;
  }
  * { margin: 0; padding: 0; box-sizing: border-box; }
  html, body { width: 1200px; height: 1000px; overflow: hidden; }
  body { background: var(--stage); position: relative; font-family: "Lato", sans-serif; }

  .card {
    position: absolute;
    width: 594px; height: 355px;
    border-radius: 12px;
  }
  .card--light { left: 303px; top: 85px; background: var(--card-light); color: var(--ink-dark); }
  .card--dark { left: 304px; top: 529px; background: var(--card-dark); color: var(--ink-light); border: 1px solid var(--card-dark-edge); }

  .holder { position: absolute; left: 38px; top: 14px; }
  .holder__name { font-family: "Montserrat", sans-serif; font-size: 20px; font-weight: 400; line-height: 1.2; }
  .holder__name b { font-weight: 600; }
  .holder__title { font-family: "Montserrat", sans-serif; font-size: 12px; }

  .brand {
    position: absolute; right: 18px; top: 180px;
    font-family: "Montserrat", sans-serif; font-size: 22px; font-weight: 400;
    letter-spacing: 0.5px; text-transform: uppercase;
  }
  .card--light .brand { color: var(--brand-teal); }
  .card--dark .brand { color: var(--ink-light); }

  .contact { position: absolute; left: 18px; top: 208px; list-style: none; }
  .contact__item { display: flex; align-items: center; height: 24px; }
  .contact__icon { width: 20px; display: flex; justify-content: center; margin-right: 15px; }
  .contact__icon svg { fill: currentColor; }
  .contact__text { font-size: 11px; letter-spacing: 0.5px; text-transform: uppercase; font-weight: 400; }
  .contact__item--address { height: 44px; }
  .contact__item--address .contact__text { font-size: 15px; font-weight: 300; line-height: 19px; }
  .contact__item--phone { height: 40px; }
  .contact__item--phone .contact__text { font-size: 25px; font-weight: 300; letter-spacing: 0; }

  .caption {
    position: absolute; left: 0; width: 1200px; text-align: center;
    font-family: "Montserrat", sans-serif; font-size: 15px; color: var(--caption);
    text-transform: uppercase;
  }
  .caption--light { top: 452px; }
  .caption--dark { top: 901px; }
</style>
</head>
<body>

<section class="card card--light">
  <div class="holder">
    <p class="holder__name">Lorem <b>ipsum</b></p>
    <p class="holder__title">Designation</p>
  </div>
  <p class="brand">Groundedpath</p>
  <ul class="contact">
    <li class="contact__item">
      <span class="contact__icon"><svg width="16" height="16" viewBox="0 0 16 16"><circle cx="8" cy="8" r="7" fill="none" stroke="currentColor" stroke-width="1.4"/><ellipse cx="8" cy="8" rx="3" ry="7" fill="none" stroke="currentColor" stroke-width="1.2"/><path d="M1 8h14M2.5 4.5h11M2.5 11.5h11" stroke="currentColor" stroke-width="1.1"/></svg></span>
      <span class="contact__text">cardstudio.example</span>
    </li>
    <li class="contact__item">
      <span class="contact__icon"><svg width="16" height="12" viewBox="0 0 16 12"><path d="M0 0h16v12H0z"/><path d="M0 0l8 6 8-6" fill="none" stroke="var(--card-light)" stroke-width="1.4"/></svg></span>
      <span class="contact__text">info@cardstudio.example</span>
    </li>
    <li class="contact__item contact__item--address">
      <span class="contact__icon"><svg width="16" height="22" viewBox="0 0 16 22"><path d="M8 0a8 8 0 0 0-8 8c0 6 8 14 8 14s8-8 8-14a8 8 0 0 0-8-8zm0 4a4 4 0 1 1 0 8 4 4 0 0 1 0-8z" fill-rule="evenodd"/></svg></span>
      <span class="contact__text">45, Linden Avenue,<br>Albany, NY 12203</span>
    </li>
    <li class="contact__item contact__item--phone">
      <span class="contact__icon"><svg width="16" height="32" viewBox="0 0 16 32"><path d="M3 0h2v6H3z"/><rect x="0" y="6" width="16" height="26" rx="2"/><rect x="3" y="10" width="10" height="9" fill="var(--card-light)"/></svg></span>
      <span class="contact__text">(555) 010.4567</span>
    </li>
  </ul>
</section>
<p class="caption caption--light">White backgroud with black text</p>

<section class="card card--dark">
  <div class="holder">
    <p class="holder__name">Lorem <b>ipsum</b></p>
    <p class="holder__title">Designation</p>
  </div>
  <p class="brand">Groundedpath</p>
  <ul class="contact">
    <li class="contact__item">
      <span class="contact__icon"><svg width="16" height="16" viewBox="0 0 16 16"><circle cx="8" cy="8" r="7" fill="none" stroke="currentColor" stroke-width="1.4"/><ellipse cx="8" cy="8" rx="3" ry="7" fill="none" stroke="currentColor" stroke-width="1.2"/><path d="M1 8h14M2.5 4.5h11M2.5 11.5h11" stroke="currentColor" stroke-width="1.1"/></svg></span>
      <span class="contact__text">cardstudio.example</span>
    </li>
    <li class="contact__item">
      <span class="contact__icon"><svg width="16" height="12" viewBox="0 0 16 12"><path d="M0 0h16v12H0z"/><path d="M0 0l8 6 8-6" fill="none" stroke="var(--card-dark)" stroke-width="1.4"/></svg></span>
      <span class="contact__text">info@cardstudio.example</span>
    </li>
    <li class="contact__item contact__item--address">
      <span class="contact__icon"><svg width="16" height="22" viewBox="0 0 16 22"><path d="M8 0a8 8 0 0 0-8 8c0 6 8 14 8 14s8-8 8-14a8 8 0 0 0-8-8zm0 4a4 4 0 1 1 0 8 4 4 0 0 1 0-8z" fill-rule="evenodd"/></svg></span>
      <span class="contact__text">45, Linden Avenue,<br>Albany, NY 12203</span>
    </li>
    <li class="contact__item contact__item--phone">
      <span class="contact__icon"><svg width="16" height="32" viewBox="0 0 16 32"><path d="M3 0h2v6H3z"/><rect x="0" y="6" width="16" height="26" rx="2"/><rect x="3" y="10" width="10" height="9" fill="var(--card-dark)"/></svg></span>
      <span class="contact__text">(555) 010.4567</span>
    </li>
  </ul>
</section>
<p class="caption caption--dark">Black backgroud with white text</p>

</body>
</html>
```